Quiet Motion Honor Project posters to attract attention at trade shows

Our company, LumaFlow, trains and certifies Tai Chi teachers. We have a project called "Quiet Motion Honor Project" and we are working with our government to provide free Tai Chi classes to military veterans. Part of what we are doing is recruiting new instructors to take our training and start teaching our Vets.<br/><br/>We will be attending Fitness conferences throughout the US during 2020 - and we have one coming up next week. I need 3 table posters 18 x 24 to catch the eye of people walking by our booth. <br/><br/>The posters should use images of Tai Chi classes, or images of Veterans or both. I was thinking one poster should attract people by saying something like: "You could make a difference in the life of a Veteran" or "Be a hero to a Hero - teaching Tai Chi to our nation's Veterans" or something like that.<br/><br/>Then I'd like a second poster to take a different approach - something like: Make $100/hour to start! Take your fitness career to the next level with a Tai Chi certification (the highest compensation in the Fitness industry). LumaFlow is recruiting instructors for your area NOW.<br/><br/>The third poster I need is one that Invites conference attendees to try a sample class. I've uploaded a sample poster in the files to give you a rough idea. I made this myself just for basic content example - but I want a much different creative vibe. Hope all this makes sense - please message me if you have questions.

Target Market(s)

Fitness conference attendees - fitness trainers, yoga teachers

Industry/Entity Type

Fitness

Font styles to use
Sans Serif

Colors

Designer to choose colors to be used in the design.

Requirements
Must have
• our logo, images of Veterans, images of fitness trainers/yoga teachers or both.Clear copy and call to action

```html
<!DOCTYPE html>
<html lang="en">
<head>
<meta charset="utf-8">
<title>Quiet Motion Honor Project – Be a Hero Poster</title>
<link rel="stylesheet" href="https://fonts.googleapis.com/css2?family=Oswald:wght@300;400&family=Caveat:wght@700&display=swap">
<style>
  :root {
    --stage: #e9ebee;
    --paper: #ffffff;
    --hero-red: #a51e22;
    --navy: #1f2a4f;
    --flag-red: #b3303a;
    --flag-white: #eef0f3;
    --uniform: #f4f4f2;
    --shadow-dark: #3a3f3a;
  }
  * { margin: 0; padding: 0; box-sizing: border-box; }
  html, body {
    width: 1200px;
    height: 923px;
    overflow: hidden;
    background: var(--stage);
  }
  .poster {
    position: absolute;
    left: 280px;
    top: 34px;
    width: 640px;
    height: 854px;
    background: var(--paper);
    overflow: hidden;
  }
  .photo {
    position: absolute;
    left: 0;
    top: 0;
    width: 640px;
    height: 854px;
  }
  .headline {
    position: absolute;
    left: 0;
    top: -4px;
    width: 640px;
    text-align: center;
    font-family: "Oswald", sans-serif;
    font-weight: 300;
    font-size: 140px;
    line-height: 1;
    letter-spacing: -2px;
    color: var(--hero-red);
  }
  .brand {
    position: absolute;
    left: 258px;
    top: 146px;
    display: flex;
    align-items: center;
    gap: 8px;
  }
  .brand-dot {
    width: 34px;
    height: 34px;
    border-radius: 50%;
    background: var(--hero-red);
  }
  .brand-name {
    font-family: "Oswald", sans-serif;
    font-weight: 400;
    font-size: 26px;
    line-height: 1;
    color: var(--hero-red);
  }
  .message {
    font-family: "Oswald", sans-serif;
    font-weight: 300;
    font-size: 74px;
    line-height: 1;
    letter-spacing: -1px;
    color: var(--navy);
  }
  .message span {
    position: absolute;
    white-space: nowrap;
  }
  .line-1 { left: 290px; top: 209px; }
  .line-2 { left: 325px; top: 294px; }
  .line-3 { left: 342px; top: 380px; }
  .line-4 { left: 360px; top: 465px; }
  .line-5 { left: 397px; top: 550px; }
  .line-6 { left: 415px; top: 635px; }
  .project-band {
    position: absolute;
    left: 0;
    top: 722px;
    width: 640px;
    height: 113px;
    background: var(--navy);
    display: flex;
    align-items: center;
    justify-content: center;
    gap: 14px;
    color: var(--paper);
  }
  .project-name {
    font-family: "Caveat", cursive;
    font-weight: 700;
    font-size: 54px;
    line-height: 1;
  }
  .star { width: 26px; height: 26px; fill: var(--paper); }
</style>
</head>
<body>
  <main class="poster">
    <svg class="photo" viewBox="0 0 640 854" role="img" aria-label="Photo of an elderly veteran in a white uniform and garrison cap holding a large American flag">
      <defs>
        <linearGradient id="veteranTone" x1="0" y1="0" x2="1" y2="1">
          <stop offset="0" stop-color="#3b3f38"/>
          <stop offset="0.45" stop-color="#c9c6c2"/>
          <stop offset="1" stop-color="#f1f1ef"/>
        </linearGradient>
        <linearGradient id="flagTone" x1="0" y1="0" x2="1" y2="1">
          <stop offset="0" stop-color="#27315c"/>
          <stop offset="0.3" stop-color="#b3303a"/>
          <stop offset="0.6" stop-color="#e7e3e4"/>
          <stop offset="1" stop-color="#a8262f"/>
        </linearGradient>
      </defs>
      <path d="M0 130 L120 150 L120 854 L0 854 Z" fill="url(#veteranTone)"/>
      <path d="M100 160 L200 185 Q250 230 300 330 L395 722 L400 854 L80 854 Z" fill="url(#flagTone)"/>
      <path d="M0 0 H640 V140 Q320 230 0 135 Z" fill="var(--paper)"/>
    </svg>

    <h1 class="headline">BE A HERO!</h1>

    <div class="brand">
      <span class="brand-dot"></span>
      <span class="brand-name">LumaFlow</span>
    </div>

    <p class="message">
      <span class="line-1">You could</span>
      <span class="line-2">make a</span>
      <span class="line-3">difference</span>
      <span class="line-4">in the life</span>
      <span class="line-5">of a</span>
      <span class="line-6">Veteran</span>
    </p>

    <div class="project-band">
      <svg class="star" viewBox="0 0 24 24" aria-hidden="true"><path d="M12 2l2.9 6.6 7.1.6-5.4 4.7 1.6 7-6.2-3.7-6.2 3.7 1.6-7L2 9.2l7.1-.6z"/></svg>
      <span class="project-name">Quiet Motion Honor Project</span>
      <svg class="star" viewBox="0 0 24 24" aria-hidden="true"><path d="M12 2l2.9 6.6 7.1.6-5.4 4.7 1.6 7-6.2-3.7-6.2 3.7 1.6-7L2 9.2l7.1-.6z"/></svg>
    </div>
  </main>
</body>
</html>
```